Flyer Design - High Quality

*** Although this current job contest is listed as a ‘one-off contest’ we are also looking at working with a graphic designer long-term, which will include quite regular design work. So even though this is just a small job, if you want to & you do a good job on this, we would love to look at working with you on a regular basis.
* The winning designer will also get a freelance job designing another flyer in same design
Job Basics:
1. the design of a ….
Promotional corporate flyer - size = A4 - approx 6 or 7 pages.
*** The design will need to be extremely high quality/professional. Must be of a similar or better standard as the attached flyers – 1) Dell Warrick_Info Pack & 2) DrOwen Pellby
* Please view these flyers first to ensure you can create a flyer of similar or better quality before proceeding.
Specific Requirements:
1. high-quality, professional promotional flyer [size = A4 - for online use predominantly . I.e. not for printing necessarily] using the text, images and basic instructions outlined on the word document attached - 'Flyer_All talks in 1_guidelines'.
2. Examples of similar quality (good) designs = 1) Dell Warrick_Info Pack & 2) DrOwen Pellby
Background:
I am a motivational speaker on health, well-being and work-life balance. This flyer is to be used for promotional purposes when clients inquire about me speaking at their conference. Dell Warrick & Owen Pellby are speakers who do somewhat similar talks to me, and who have flyers that I really like.
Theme: My general theme is ‘health and well-being’ (we're a little bit more towards natural health and Eastern medicine, but don't want it too ‘eastern’ if you know what I mean).
Main Look & Feel … to be conveyed:
Professional / Corporate
Health, Vitality and happiness (fresh, modern and vital)
eye-catching / attention grabbing
* The design should represent a balance between highly sophisticated, professional and classy - corporate savvy - with a hint of 'natural health, Eastern wisdom and a general ‘high energy/fresh health and vitality feel'. While we would like the design to convey some aspect of ‘ natural/Eastern’ wisdom), we predominantly want to convey the idea of ‘modern’ health (i.e. fresh, modern and vital).
Colours:
We are open to your creative suggestions, but were generally thinking something along the lines of the colours in our corporate logo –
dark blue, aqua blue, grey – see logo (QEV_300kb.jpg) in attachments
- possibly with some bright green, orange etc if you think it might suit – to help give it the ‘natural health’ feel.
* Notes:
1. SAVING YOUR TIME: If you just want to start just doing a quickish design of the first 1-2 pages and submitting that (images for these pages attached - though use own images if you think they are better), then that’s fine. Then we can let you know if it is along the lines of something we like or not. This way, you can do something relatively quickly, without wasting too much time, if it is definitely not something we like. Hope that helps - we are always conscious of trying to make things good for you as a designer too.
2. Do not feel completely bound to the ideas suggested/asked for. Feel free to convey the basic ideas/keys but feel free to use/follow some of your own ideas/creative desires.
3. Any photos/images should be royalty free (or ask us if we want to pay for it) and not widely used or seen in the public domain - i.e. we don’t want people to have seen the photo/image elsewhere (within reason).
Thanks a lot and look forward to receiving your first design!
Cheers
Tobin
Predominantly corporates / business groups.
Graphic Designer

```html
<!DOCTYPE html>
<html lang="en">
<head>
<meta charset="utf-8">
<title>Tobin – Speaking Sessions</title>
<link rel="stylesheet" href="https://fonts.googleapis.com/css2?family=Roboto+Condensed:wght@300;400;700&family=Dancing+Script&display=swap">
<style>
:root{
  --page:#ffffff;
  --panel:#84c3ea;
  --panel-shadow:rgba(0,0,0,.28);
  --ink:#ffffff;
  --badge-ink:#5aa8dc;
  --quote:#7fa6c9;
  --photo-sky:#a9cbe6;
  --photo-office:#8c7f70;
  --photo-shore:#9fb9cb;
}
*{margin:0;padding:0;box-sizing:border-box}
html,body{width:1200px;height:900px;overflow:hidden;background:var(--page)}
body{position:relative;font-family:"Roboto Condensed",Arial,sans-serif;color:var(--ink)}
.spread{position:absolute;left:40px;top:170px;width:1120px;height:560px;background:var(--panel);box-shadow:0 6px 10px var(--panel-shadow)}
.abs{position:absolute}
.rule{position:absolute;height:1.5px;background:var(--ink)}
.intro{font-size:12px;font-weight:300;white-space:nowrap}
.legend{font-size:11.5px;font-weight:300;display:flex;align-items:center;gap:4px;white-space:nowrap}
.legend .badge{margin-right:3px}
.legend .gap{width:14px}
.badge{display:inline-flex;align-items:center;justify-content:center;width:14px;height:14px;border-radius:50%;background:var(--ink);color:var(--badge-ink);font-size:6.5px;font-weight:700;vertical-align:middle}
.title{font-size:29px;font-weight:300;white-space:nowrap;letter-spacing:-.3px;display:flex;align-items:center}
.title .num{font-weight:700;margin-right:6px}
.title .badges{display:inline-flex;gap:1px;margin-left:3px;margin-top:8px}
.subhead{font-size:13.5px;font-weight:700;white-space:nowrap}
.desc{font-size:8.6px;font-weight:300;line-height:1.25;white-space:nowrap}
.desc.large{font-size:9.4px}
.photo{position:absolute;width:164px;height:117px;border-radius:13px}
.photo.sky{background:var(--photo-sky)}
.photo.office{background:var(--photo-office)}
.photo.shore{background:var(--photo-shore)}
.includes{font-size:10.5px;font-weight:300;line-height:14.2px;white-space:nowrap}
.includes h4{font-weight:300;font-size:10.5px}
.includes ul{list-style:none}
.includes li{padding-left:8px;text-indent:-8px}
.includes li::before{content:"• "}
.quote{position:absolute;left:500px;top:455px;width:620px;height:105px}
.quote text{font-family:"Dancing Script",cursive;font-size:21px;fill:var(--quote)}
</style>
</head>
<body>
<main class="spread">
  <div class="rule" style="left:23px;top:30px;width:450px"></div>
  <p class="abs intro" style="left:27px;top:38px">Tobin’s thought provoking talks and sessions are delivered in formats tailored to your requirements.</p>
  <p class="abs legend" style="left:27px;top:59px"><span class="badge">K</span>Keynote - 40-90mins<span class="gap"></span><span class="badge">WB</span>Workshop or Breakout<span class="gap"></span><span class="badge">HD</span>Half Day Session</p>
  <div class="rule" style="left:23px;top:83px;width:450px"></div>

  <!-- Session 1 -->
  <h2 class="abs title" style="left:22px;top:101px"><span class="num">1</span>Achieve Your ‘Natural High’<span class="badges"><span class="badge">K</span><span class="badge">WB</span><span class="badge">HD</span></span></h2>
  <h3 class="abs subhead" style="left:24px;top:143px">Enjoy high energy, low stress, life balance &amp; work success…everyday</h3>
  <p class="abs desc" style="left:24px;top:162px">The perfect high energy, high content session that outlines the keys to ongoing healthy performance – diet, exercise, sleep, stress management<br>and personal motivation. Includes an understanding of everyone’s ‘natural performance cycles’ and age-old wisdoms of health.</p>
  <div class="photo sky" style="left:26px;top:192px" role="img" aria-label="Photo of two people leaping joyfully outdoors"></div>
  <div class="abs includes" style="left:201px;top:193px">
    <h4>INCLUDES:</h4>
    <ul>
      <li>how to reduce stress &amp; increase vitality…by up to 30%</li>
      <li>how to maximise mental focus, enjoy a calm mind &amp;<br>experience more work-flow</li>
      <li>the 3 simple, everyday tips for losing weight, being<br>happier &amp; enjoying work more</li>
      <li>why ‘doing things we love’ is scientifically healthier<br>than any diet or exercise regime</li>
    </ul>
  </div>

  <!-- Session 2 -->
  <h2 class="abs title" style="left:22px;top:333px"><span class="num">2</span>Your Work-Life Balance High<span class="badges"><span class="badge">K</span><span class="badge">WB</span><span class="badge">HD</span></span></h2>
  <h3 class="abs subhead" style="left:24px;top:373px">How to achieve high-level work success … while still having a life!</h3>
  <p class="abs desc" style="left:24px;top:391px">A highly popular, high-motivation session showing people a 7 step process for achieving a healthier ‘work-life balance’ while<br>maximising their work performance and results.</p>
  <div class="photo sky" style="left:26px;top:420px" role="img" aria-label="Photo of two business people jumping in the air outdoors"></div>
  <div class="abs includes" style="left:201px;top:424px">
    <h4>INCLUDES:</h4>
    <ul>
      <li>how to improve day-to-day productivity by 20% +</li>
      <li>how to create more time &amp; set boundaries to get ‘what’s<br>really important’ done</li>
      <li>how to structure their day (re; daily cycles) to enjoy<br>maximum energy &amp; focus</li>
      <li>achieve the real goal – work success while still having<br>(and enjoying) a life</li>
    </ul>
  </div>

  <!-- Session 3 -->
  <h2 class="abs title" style="left:580px;top:27px"><span class="num">3</span>Work Smarter Not Harder<span class="badges"><span class="badge">K</span><span class="badge">WB</span></span></h2>
  <h3 class="abs subhead" style="left:584px;top:68px">How to do 20% more in 20% less time … with 20% less stress</h3>
  <p class="abs desc" style="left:584px;top:87px">Also promoted as ‘Beat the ‘Busyness’ of Business - The most sought-after session on motivation, time management and productivity. A highly<br>practical, ‘hands-on’ session that teaches people the 7 peak productivity practices of the world’s most successful individuals / businesspeople.</p>
  <div class="photo office" style="left:586px;top:117px" role="img" aria-label="Photo of an office team joining hands over a meeting table"></div>
  <div class="abs includes" style="left:761px;top:119px">
    <h4>INCLUDES:</h4>
    <ul>
      <li>how to cultivate the ‘high performance state’<br>or ‘flow state’ to do more in less time</li>
      <li>to use (and control) technology (email, phones) to save time …&amp; stress</li>
      <li>the secrets of world leaders such as Lena Marchetti,<br>Harold Vance &amp; Quentin Aldous</li>
      <li>how to do 20% more in 20% less time … with 20% less stress<br>…guaranteed!</li>
    </ul>
  </div>

  <!-- Session 4 -->
  <h2 class="abs title" style="left:580px;top:256px"><span class="num">4</span>Less Stress Work Success<span class="badges"><span class="badge">K</span><span class="badge">WB</span><span class="badge">HD</span></span></h2>
  <h3 class="abs subhead" style="left:584px;top:297px">everyday tools for managing stress within a hectic work-life</h3>
  <p class="abs desc large" style="left:584px;top:315px">A practical, hands-on session that shows people how to go beyond merely ‘managing’ stress to promoting their natural<br>‘stress-resistant’ state and high performance despite busy or high-pressure environments.</p>
  <div class="photo shore" style="left:586px;top:344px" role="img" aria-label="Photo of a businessman with a briefcase standing in the surf at the shoreline"></div>
  <div class="abs includes" style="left:761px;top:347px">
    <h4>INCLUDES:</h4>
    <ul>
      <li>1 minute office techniques to calm the mind and relax the body</li>
      <li>the keys to a good nights sleep &amp; how to ‘switch-off’ an overactive mind</li>
      <li>breathing techniques to dissolve tension &amp; optimise mental performance</li>
      <li>simple tips for enjoying a ‘happy-high’ state of wellbeing</li>
    </ul>
  </div>

  <svg class="quote" viewBox="0 0 620 105" aria-label="Testimonial quote">
    <path id="quote-curve" d="M8 50 C 70 85 140 90 250 55 S 470 0 610 70" fill="none"/>
    <text><textPath href="#quote-curve">“One of the best sessions on health and well-being I have ever seen” Rosalind Teague</textPath></text>
  </svg>
</main>
</body>
</html>
```